Health Benefits Association Website Design

The Allied Household Provision Association (AHPA) is an organization formed for the purpose of providing its members better value for selected health benefits and services. Members can use the association benefits either in conjunction with or independently of other medical insurance they may have. Some of the benefits available include discounted dental and vision care and prescription mail order services. There is no limitation on who can join. This membership will be primarily marketed as a way to enhance the value of a fixed benefit health insurance plan although members do not have to have the insurance plan join the association.

We are seeking a design for a website to be used for consumers to get information about membership and for current members to be able to access their benefits. The website should include:

1) A landing page to provide a description of the AHPA

2) A secondary page that can be duplicated that will:
a. Provide a list of benefits
b. Provide a membership enrollment form
c. Provide a member’s only access page
d. Provide a contact page for more information

We are seeking a modern but conservative design that will reflect value, simplicity and good health. The site design will also need to be compatible for use with mobile phones and tablets.

A copy of the association logo is included with the submission. It will also need to be incorporated into the website design. Layouts of similar association websites have also been included for reference.

Target Market(s)

Ages 25 to 65 unmarried, married with no children, professionals, self-employed, active and healthy

Industry/Entity Type

Health And Wellness

Number of Pages Required

2 page

Font styles to use
Sans Serif

Colors

Designer to choose colors to be used in the design.

Requirements
Must have
• AHPA Logo (attached). Use colors from the logo in the website design.
Nice to have
• Graphics, if used, should convey health and fitness and skew toward a diverse array of adults 25 to 40.

```html
<!DOCTYPE html>
<html lang="en">
<head>
<meta charset="utf-8">
<title>Allied Household Provision Association</title>
<link rel="stylesheet" href="https://fonts.googleapis.com/css2?family=Arimo:wght@400;700&display=swap">
<style>
:root{
  --yellow:#f6c900;
  --olive:#a3ab62;
  --olive-dark:#7f8a3c;
  --olive-soft:#b7bd80;
  --ink:#111111;
  --white:#ffffff;
  --black:#000000;
  --rule:#b9b35a;
}
*{box-sizing:border-box;margin:0;padding:0}
html,body{width:1200px;height:2980px;overflow:hidden;background:var(--white)}
body{position:relative;font-family:"Arimo",Arial,sans-serif;color:var(--ink);font-weight:700}
.abs{position:absolute}
.btn{position:absolute;background:var(--yellow);color:var(--white);font-weight:700;display:flex;align-items:center;justify-content:center;border-radius:3px;white-space:nowrap}

/* header */
.brand-box{left:236px;top:0;width:106px;height:114px;background:var(--white);border-radius:0 0 6px 6px;box-shadow:0 2px 6px rgba(0,0,0,.25);z-index:3;display:flex;align-items:center;justify-content:center;text-align:center;padding:8px}
.brand-name{font-size:12px;line-height:14px;color:var(--olive-dark);font-weight:700}
.nav{left:0;top:0;width:1200px;height:62px;background:var(--white);z-index:2}
.nav a{position:absolute;top:22px;font-size:13px;color:var(--ink);text-decoration:none}
.join{left:802px;top:18px;width:170px;height:24px;font-size:11px;border-radius:4px;justify-content:flex-start;padding-left:22px;z-index:3}
.free-dot{left:934px;top:13px;width:34px;height:34px;border-radius:50%;background:var(--olive);color:var(--white);font-size:10px;display:flex;align-items:center;justify-content:center;z-index:4;transform:rotate(-15deg)}

/* hero */
.hero-photo{left:0;top:62px;width:1200px;height:420px;background:linear-gradient(100deg,#4d6a35 0%,#7c8c4a 35%,#c99f86 55%,#6d8a4a 80%,#3c5a2a 100%)}
.hero-curve{left:0;top:440px;width:1200px;height:60px}
.hero-kicker{left:298px;top:220px;font-size:13px;color:var(--yellow)}
.hero-title{left:298px;top:240px;font-size:31px;line-height:29px;color:var(--yellow)}
.login{left:300px;top:342px;width:170px;height:32px;font-size:13px}
.arrow{top:250px}

/* section heading */
.heading{left:0;width:1200px;display:flex;align-items:center;justify-content:center;gap:0}
.heading .line{width:100px;height:2px;background:var(--rule)}
.heading .dot{width:16px;height:16px;border-radius:50%;background:var(--yellow);margin:0 20px}
.heading h2{font-size:34px;font-weight:700}

/* about */
.about-text{left:236px;top:634px;width:298px;font-size:12.4px;line-height:14.6px}
.about-photo{left:550px;top:638px;width:420px;height:184px;background:linear-gradient(120deg,#4a4037,#8f8a86 40%,#c9d2dc 70%,#6e7480)}

/* bands */
.band{left:0;width:1200px}
.band-title{left:0;width:1200px;text-align:center;color:var(--white)}

/* benefits */
.card-photo{top:1310px;width:170px;height:170px;border-radius:4px}
.card-cap{top:1492px;width:170px;font-size:12.5px;line-height:15px}

/* news */
.news-photo{top:2092px;width:170px;height:170px;border-radius:3px}
.news-text{top:2096px;width:168px;font-size:12.4px;line-height:14.7px}
.pager{top:2298px;width:32px;height:32px}

/* footer */
.footer{left:0;top:2708px;width:1200px;height:272px;background:var(--black);color:var(--white)}
.foot-h{top:72px;font-size:17px;color:var(--yellow)}
.foot-list{top:104px;font-size:13px;line-height:23px;list-style:none}
.email{left:488px;top:102px;width:234px;height:26px;background:var(--white);border-radius:4px;font-size:11px;color:#777;padding:7px 8px;font-weight:400}
.send{left:672px;top:102px;width:50px;height:26px;background:var(--yellow);border-radius:4px}
.foot-note{left:488px;top:148px;width:250px;font-size:13px;line-height:15px}
.foot-brand{left:800px;top:50px;width:172px;height:180px;display:flex;align-items:center;justify-content:center;text-align:center;font-size:22px;line-height:27px;color:var(--white)}
</style>
</head>
<body>

<div class="abs nav">
  <a style="left:360px">Home</a>
  <a style="left:448px">Benefits</a>
  <a style="left:534px">Membership</a>
  <a style="left:654px">News</a>
  <a style="left:738px">Contact</a>
</div>
<div class="abs brand-box"><span class="brand-name">Allied Household Provision Association</span></div>
<div class="btn join">Join Membership</div>
<div class="abs free-dot">Free</div>

<div class="abs hero-photo" role="img" aria-label="Smiling mature couple outdoors in a sunny garden"></div>
<svg class="abs hero-curve" viewBox="0 0 1200 60" preserveAspectRatio="none"><path d="M0 38 Q600 0 1200 38 L1200 60 L0 60 Z" fill="#ffffff"/></svg>
<svg class="abs arrow" style="left:188px" width="40" height="58" viewBox="0 0 40 58"><path d="M32 4 L8 29 L32 54" fill="none" stroke="#f6c900" stroke-width="7"/><path d="M36 4 L12 29 L36 54" fill="none" stroke="#111" stroke-width="2"/></svg>
<svg class="abs arrow" style="left:976px" width="40" height="58" viewBox="0 0 40 58"><path d="M8 4 L32 29 L8 54" fill="none" stroke="#f6c900" stroke-width="7"/><path d="M4 4 L28 29 L4 54" fill="none" stroke="#111" stroke-width="2"/></svg>
<div class="abs hero-kicker">Lorem Ipsum is simply dummy text</div>
<div class="abs hero-title">Lorem Ipsum<br>is simply dummy<br>text</div>
<div class="btn login">Login</div>

<div class="abs heading" style="top:538px"><span class="line"></span><span class="dot"></span><h2>ABOUT US</h2><span class="dot"></span><span class="line"></span></div>
<p class="abs about-text">The Allied Household Provision Association (AHPA) is an organization formed for the purpose of providing its members better value for selected health benefits and services. Members can use the association benefits either in conjunction with or independently of other medical insurance they may have. Some of the benefits available include discounted dental and vision care and prescription mail order services. There is no limitation on who can join. This membership will be primarily marketed as a way to enhance the value of a fixed benefit health</p>
<div class="abs about-photo" role="img" aria-label="Business team gathered around a tablet in an office"></div>

<svg class="abs band" style="top:868px" width="1200" height="316" viewBox="0 0 1200 316" preserveAspectRatio="none" role="img" aria-label="Group of cheerful older adults raising their arms outdoors, tinted olive">
  <defs><linearGradient id="g1" x1="0" x2="1"><stop offset="0" stop-color="#b3b07a"/><stop offset=".5" stop-color="#a3ab62"/><stop offset="1" stop-color="#98a35a"/></linearGradient></defs>
  <path d="M0 14 Q600 -6 1200 14 L1200 316 L0 316 Z" fill="url(#g1)"/>
</svg>
<div class="abs band-title" style="top:976px;font-size:13px">Lorem Ipsum is simply dummy text</div>
<div class="abs band-title" style="top:994px;font-size:34px">Lorem Ipsum is simply</div>
<div class="btn" style="left:486px;top:1066px;width:170px;height:32px;font-size:12px">More</div>

<div class="abs heading" style="top:1240px"><span class="line"></span><span class="dot"></span><h2>Benefits</h2><span class="dot"></span><span class="line"></span></div>
<div class="abs card-photo" style="left:236px;background:linear-gradient(135deg,#8c9650,#b5a273,#9aa35e)" role="img" aria-label="Diverse group of smiling adults"></div>
<div class="abs card-photo" style="left:426px;background:linear-gradient(135deg,#e6e4df,#c7a98b,#f0ede8)" role="img" aria-label="Couple talking at a bright dining table"></div>
<div class="abs card-photo" style="left:614px;background:linear-gradient(135deg,#8a6f4e,#e0b38c,#d9d5cf)" role="img" aria-label="Man on the phone at a laptop"></div>
<div class="abs card-photo" style="left:802px;background:linear-gradient(180deg,#f4b21b,#e07812,#7a2d08)" role="img" aria-label="Runners silhouetted against a sunset"></div>
<div class="abs card-cap" style="left:236px">Lorem Ipsum is simply dummy text</div>
<div class="abs card-cap" style="left:426px">Lorem Ipsum is simply dummy text</div>
<div class="abs card-cap" style="left:614px">Lorem Ipsum is simply dummy text</div>
<div class="abs card-cap" style="left:802px">Lorem Ipsum is simply dummy text</div>
<div class="btn" style="left:518px;top:1554px;width:168px;height:32px;font-size:12px">More</div>

<svg class="abs band" style="top:1648px" width="1200" height="308" viewBox="0 0 1200 308" preserveAspectRatio="none" role="img" aria-label="Ring of figures holding hands, tinted olive">
  <defs><radialGradient id="g2" cx=".5" cy=".6" r=".7"><stop offset="0" stop-color="#aab36c"/><stop offset="1" stop-color="#97a257"/></radialGradient></defs>
  <path d="M0 8 Q600 -6 1200 8 L1200 308 L0 308 Z" fill="url(#g2)"/>
</svg>
<div class="abs band-title" style="top:1742px;font-size:32px">Enjoy our benefits</div>
<div class="btn" style="left:460px;top:1804px;width:288px;height:44px;font-size:18px">Become a member</div>

<div class="abs heading" style="top:2016px"><span class="line"></span><span class="dot"></span><h2>News</h2><span class="dot"></span><span class="line"></span></div>
<div class="abs news-photo" style="left:236px;background:radial-gradient(circle at 45% 40%,#d9d3a6,#97a25a 70%)" role="img" aria-label="Close-up of an eye behind a lens"></div>
<p class="abs news-text" style="left:426px">Lorem Ipsum is simply dummy text of the printing and typesetting industry. Lorem Ipsum has been the industry's standard dummy text ever since the 1500s, when an unknown printer took a galley of type and scrambled it to make a type specimen book. It has</p>
<div class="abs news-photo" style="left:614px;background:linear-gradient(135deg,#dfe6ec,#e9c7b5,#f3efe9)" role="img" aria-label="Patient at a dental check-up"></div>
<p class="abs news-text" style="left:802px">Lorem Ipsum is simply dummy text of the printing and typesetting industry. Lorem Ipsum has been the industry's standard dummy text ever since the 1500s, when an unknown printer took a galley of type and scrambled it to make a type specimen book. It has</p>
<svg class="abs pager" style="left:562px" viewBox="0 0 32 32"><circle cx="16" cy="16" r="16" fill="#8a9340"/><path d="M19 9 L12 16 L19 23" fill="none" stroke="#fff" stroke-width="3.5"/></svg>
<svg class="abs pager" style="left:612px" viewBox="0 0 32 32"><circle cx="16" cy="16" r="16" fill="#8a9340"/><path d="M13 9 L20 16 L13 23" fill="none" stroke="#fff" stroke-width="3.5"/></svg>

<svg class="abs band" style="top:2392px" width="1200" height="316" viewBox="0 0 1200 316" preserveAspectRatio="none" role="img" aria-label="Faint world map on olive background">
  <path d="M0 18 Q600 -10 1200 18 L1200 316 L0 316 Z" fill="#a3ab62"/>
</svg>
<div class="abs band-title" style="top:2446px;font-size:32px">Get in touch</div>
<p class="abs" style="left:236px;top:2496px;width:736px;font-size:11.6px;line-height:13px;color:#fff;text-align:left">Lorem Ipsum is simply dummy text of the printing and typesetting industry. Lorem Ipsum has been the industry's standard dummy text ever since the 1500s, when an unknown printer took a galley of type and scrambled it to make a type specimen book. It has survived not only five centuries, but also the leap into electronic typesetting, remaining essentially unchanged. It was popularised in the 1960s with the release of Lettersheet sheets containing Lorem Ipsum passages, and more recently with desktop publishing software like Pagecraft Studio including versions of Lorem Ipsum.</p>
<div class="btn" style="left:460px;top:2600px;width:288px;height:44px;font-size:18px">Contact us</div>

<footer class="abs footer">
  <div class="abs foot-h" style="left:236px">Menus</div>
  <ul class="abs foot-list" style="left:236px"><li>Home</li><li>About us</li><li>Benefits</li><li>Membership</li><li>News</li><li>Contact</li></ul>
  <div class="abs foot-h" style="left:362px">Follow us</div>
  <ul class="abs foot-list" style="left:362px">
    <li><span style="display:inline-block;width:10px;height:10px;background:#fff;margin-right:8px"></span>Friendbook</li>
    <li><span style="display:inline-block;width:10px;height:10px;background:#fff;margin-right:8px"></span>Chirper</li>
    <li><span style="display:inline-block;width:10px;height:10px;background:#fff;margin-right:8px"></span>Snapgram</li>
  </ul>
  <div class="abs foot-h" style="left:488px">Subscribe to our newsletter</div>
  <div class="abs email">Your Email</div>
  <div class="abs send"><svg width="50" height="26" viewBox="0 0 50 26"><path d="M17 13 L34 6 L29 20 L25 15 Z" fill="#fff"/></svg></div>
  <p class="abs foot-note">Lorem Ipsum is simply dummy text of the printing and typesetting containing Lorem Ipsum passages, and more recently with</p>
  <div class="abs foot-brand">Allied Household Provision Association</div>
</footer>

</body>
</html>
```